Bed & Breakfast Business Card Design

Casa Mirador Bed & Breakfast is a private, adult-only, upscale retreat for guests vacationing or on business in the Atlanta area.

Event venue for weddings & retreats

Target Market(s)

Age 40+ couples, romantic get-aways, honeymoon, small weddings, business retreats

Industry/Entity Type

Business

Contact Information for Business Card

Casa Mirador Bed & Breakfast, LLC
7208 Bramwick Ferry Road
Ashgrove, GA 30999
770-555-0193
www.CasaMiradorRetreat-example.com

```html
<!DOCTYPE html>
<html lang="en">
<head>
<meta charset="utf-8">
<title>Casa Mirador Bed &amp; Breakfast – Business Card</title>
<link rel="stylesheet" href="https://fonts.googleapis.com/css2?family=Questrial&display=swap">
<style>
  :root {
    --stage: #000000;
    --card-white: #ffffff;
    --brand-green: #8ba83a;
    --brand-red: #c83a30;
    --cream: #f4efd9;
    --night-top: #1e2c52;
    --night-mid: #3a4660;
    --warm-glow: #b88a55;
    --pool: #2d5f66;
  }
  * { box-sizing: border-box; margin: 0; padding: 0; }
  html, body { width: 1200px; height: 827px; overflow: hidden; background: var(--stage); }
  .canvas { position: relative; width: 1200px; height: 827px; }

  .card { position: absolute; overflow: hidden; }

  /* Front */
  .card-front { left: 112px; top: 50px; width: 635px; height: 363px; }
  .front-photo {
    position: absolute; inset: 0;
    background: linear-gradient(180deg, var(--night-top) 0%, var(--night-mid) 45%, var(--warm-glow) 66%, #6b5a45 78%, var(--pool) 90%, #1f3e44 100%);
  }
  .front-brand {
    position: absolute; left: 0; right: 0; top: 48px; text-align: center;
    font-family: "Questrial", sans-serif; font-weight: 400; color: var(--cream);
  }
  .front-name { font-size: 50px; font-weight: 400; line-height: 1; }
  .front-tag { font-size: 27px; letter-spacing: 1px; margin-top: 10px; }

  /* Back */
  .card-back { left: 440px; top: 385px; width: 640px; height: 365px; background: var(--card-white); }
  .back-orchid {
    position: absolute; right: 30px; top: 0; width: 170px; height: 365px;
    background: radial-gradient(ellipse at 55% 62%, #f4f4f1 0%, #e4e4df 45%, #ffffff 80%);
  }
  .back-brand {
    position: absolute; left: 70px; top: 40px;
    font-family: "Questrial", sans-serif; font-weight: 400; color: var(--brand-green);
  }
  .back-name { font-size: 50px; font-weight: 400; line-height: 1; }
  .back-tag { font-size: 26px; letter-spacing: 1px; margin-top: 12px; padding-left: 30px; }
  .contact {
    position: absolute; left: 34px; top: 200px; list-style: none;
    font-family: "Questrial", sans-serif; font-size: 22px; color: var(--brand-red); line-height: 31px;
  }
  .contact li { display: flex; align-items: center; }
  .contact .icon { width: 22px; height: 22px; margin-right: 14px; flex: none; }
  .contact .plain { padding-left: 36px; }
</style>
</head>
<body>
<main class="canvas">

  <section class="card card-front" aria-label="Business card front">
    <div class="front-photo" role="img" aria-label="Night photograph of the bed and breakfast courtyard with lit stucco walls, tiled pavilion and pool under a starry sky"></div>
    <div class="front-brand">
      <h1 class="front-name">Casa Mirador</h1>
      <p class="front-tag">BED &amp; BREAKFAST</p>
    </div>
  </section>

  <section class="card card-back" aria-label="Business card back">
    <div class="back-orchid" role="img" aria-label="Photograph of a white orchid stem"></div>
    <div class="back-brand">
      <h2 class="back-name">Casa Mirador</h2>
      <p class="back-tag">BED &amp; BREAKFAST</p>
    </div>
    <ul class="contact">
      <li class="plain">7208 Bramwick Ferry Road</li>
      <li class="plain">Ashgrove, GA 30999</li>
      <li>
        <svg class="icon" viewBox="0 0 24 24" aria-hidden="true"><path fill="#c83a30" d="M6.6 2.5l3 3.2-1.8 2.4c1.3 2.8 3.4 5 6.2 6.3l2.3-1.8 3.2 3-2 3.4C10 18.7 5.3 14 4 4.5z"/></svg>
        770-555-0193
      </li>
      <li>
        <svg class="icon" viewBox="0 0 24 24" aria-hidden="true"><rect x="2" y="3" width="20" height="13" rx="1" fill="none" stroke="#c83a30" stroke-width="2.4"/><rect x="10" y="16" width="4" height="4" fill="#c83a30"/><rect x="6" y="20" width="12" height="2" fill="#c83a30"/></svg>
        www.CasaMiradorRetreat-example.com
      </li>
    </ul>
  </section>

</main>
</body>
</html>
```